依頼概要
ふわりやと言うめろんぱんチェンーのキャンペーン商品のポスター依頼です。
昨年も販売した商品で今年も6月から期間限定で販売します。
商品名 小春ミントメロンパン
売価  320円
サイズ B2
ポスターに求める事は、夏場の暑い時期に見ても、さっぱりした感じのするポスターをお願いしたいと思います。店舗と商品のイメージはHPをご覧になって下さい。
ファイルは、そのままネット印刷会社に依頼できる状態のファイルとCS2で編集可能なアウトライン前のファイルと出して頂ける事を条件とします。

瀬戸内のブランドイメージの表現と夏の感じが強く感じられ、商品も遠目から瞬間的に認識で、訴求につながると選考したスッタフの意見となりました。

沢山のご応募頂き有難うございました。
最終の選考に5人の方を絞り、いずれもお願いしたいくらい素晴らし作品でした。また次は、秋の商品・新商品を検討しております。
今後とも宜しくお願い致します。

```html
<!DOCTYPE html>
<html lang="ja">
<head>
<meta charset="utf-8">
<title>小春ミントメロンパン 限定販売</title>
<link rel="stylesheet" href="https://fonts.googleapis.com/css2?family=M+PLUS+Rounded+1c:wght@500;700;800;900&display=swap">
<style>
  :root {
    --cream: #fbf8e8;
    --pattern-yellow: #f6e37a;
    --pattern-green: #cfe6a4;
    --green: #7bc043;
    --green-dark: #4f9a2a;
    --white: #ffffff;
    --ink: #5a4630;
    --slice: #f6d63a;
    --bun-light: #f3d58a;
    --bun-deep: #dca246;
  }
  html, body {
    margin: 0;
    padding: 0;
    width: 846px;
    height: 1200px;
    overflow: hidden;
  }
  body {
    font-family: "M PLUS Rounded 1c", sans-serif;
    color: var(--ink);
  }
  .poster {
    position: relative;
    width: 846px;
    height: 1200px;
    overflow: hidden;
    background: var(--cream);
  }
  .background-pattern {
    position: absolute;
    inset: 0;
    background:
      radial-gradient(ellipse at 50% 52%, var(--cream) 0%, var(--cream) 48%, rgba(251,248,232,0) 72%),
      linear-gradient(135deg, var(--pattern-yellow) 0%, var(--pattern-green) 50%, var(--pattern-yellow) 100%);
    opacity: 0.75;
  }
  .title {
    position: absolute;
    left: 0;
    top: 60px;
    width: 846px;
    margin: 0;
    font-weight: 900;
    color: var(--green);
    -webkit-text-stroke: 14px var(--white);
    paint-order: stroke fill;
    text-shadow: 0 6px 10px rgba(90, 70, 48, 0.18);
    line-height: 1;
    transform: rotate(-4deg);
    transform-origin: 50% 50%;
  }
  .title-line {
    display: block;
    white-space: nowrap;
  }
  .title-line--first {
    font-size: 104px;
    padding-left: 110px;
    letter-spacing: 2px;
  }
  .title-line--second {
    font-size: 100px;
    padding-left: 170px;
    margin-top: 14px;
    letter-spacing: 2px;
  }
  .slice-accent {
    position: absolute;
    left: 560px;
    top: 268px;
    width: 90px;
    height: 90px;
  }
  .limited-badge {
    position: absolute;
    left: 630px;
    top: 318px;
    width: 148px;
    height: 148px;
    border-radius: 50%;
    background: var(--white);
    border: 6px solid var(--green);
    box-sizing: border-box;
    display: flex;
    align-items: center;
    justify-content: center;
    transform: rotate(8deg);
  }
  .limited-badge span {
    font-weight: 900;
    font-size: 38px;
    line-height: 1.1;
    color: var(--green);
    text-align: center;
  }
  .product-photo {
    position: absolute;
    left: 160px;
    top: 360px;
    width: 480px;
    height: 400px;
  }
  .price {
    position: absolute;
    left: 420px;
    top: 730px;
    display: flex;
    align-items: flex-end;
    gap: 6px;
    transform: rotate(-7deg);
    transform-origin: left bottom;
    color: var(--green);
    -webkit-text-stroke: 8px var(--white);
    paint-order: stroke fill;
  }
  .price-amount {
    font-weight: 900;
    font-size: 104px;
    line-height: 1;
  }
  .price-tax {
    font-weight: 800;
    font-size: 24px;
    line-height: 1;
    margin-bottom: 14px;
    -webkit-text-stroke: 5px var(--white);
  }
  .description {
    position: absolute;
    left: 0;
    top: 885px;
    width: 846px;
    margin: 0;
    text-align: center;
    font-weight: 800;
    font-size: 28px;
    line-height: 1.45;
    color: var(--ink);
    transform: rotate(-4deg);
  }
  .description .highlight {
    color: var(--green-dark);
  }
  .brand {
    position: absolute;
    left: 0;
    top: 1060px;
    width: 846px;
    display: flex;
    flex-direction: column;
    align-items: center;
  }
  .brand-row {
    display: flex;
    align-items: center;
    gap: 12px;
  }
  .brand-dot {
    width: 44px;
    height: 44px;
    border-radius: 50%;
    background: var(--bun-light);
  }
  .brand-name {
    font-weight: 800;
    font-size: 44px;
    color: var(--ink);
    line-height: 1;
  }
  .brand-tagline {
    margin-top: 8px;
    font-weight: 700;
    font-size: 16px;
    color: var(--ink);
  }
</style>
</head>
<body>
  <main class="poster">
    <div class="background-pattern" role="img" aria-label="柑橘と葉の散らし模様の背景"></div>

    <h1 class="title">
      <span class="title-line title-line--first">小春ミント</span>
      <span class="title-line title-line--second">メロンパン</span>
    </h1>

    <svg class="slice-accent" viewBox="0 0 90 90" role="img" aria-label="輪切りの柑橘のイラスト">
      <circle cx="45" cy="45" r="42" fill="var(--slice)" stroke="#ffffff" stroke-width="5"/>
    </svg>

    <div class="limited-badge"><span>限定<br>販売</span></div>

    <svg class="product-photo" viewBox="0 0 480 400" role="img" aria-label="ホイップクリームとミントクリームをサンドしたメロンパンの写真">
      <defs>
        <radialGradient id="bunTone" cx="45%" cy="35%" r="70%">
          <stop offset="0%" stop-color="#f3d58a"/>
          <stop offset="100%" stop-color="#dca246"/>
        </radialGradient>
      </defs>
      <ellipse cx="240" cy="200" rx="236" ry="196" fill="url(#bunTone)"/>
    </svg>

    <div class="price">
      <span class="price-amount">¥320</span>
      <span class="price-tax">税込</span>
    </div>

    <p class="description">
      風味が爽やかな<br>
      <span class="highlight">小春ミント</span>と<span class="highlight">ホイップクリーム</span>を<br>
      ふわりやメロンにサンドしました
    </p>

    <div class="brand">
      <div class="brand-row">
        <span class="brand-dot"></span>
        <span class="brand-name">ふわりや</span>
      </div>
      <span class="brand-tagline">まいにち焼きたて、やさしい味をどうぞ</span>
    </div>
  </main>
</body>
</html>
```